Reel Harbor - Premier Angling Expeditions needs a one of a kind Flyer/Brochure

We need a bold, professional and confident Flyer to help us Brand and advertise what we do for companies and teams.

We Make It Easy for you to Plan Your Next Company Adventure

Reel Harbor specializes in customizing Fishing Adventures for Corporate Teams, Executive Retreats, and VIP Clients.

- Reel Harbor takes care of all the planning, preparation and logistics for all your corporate fishing adventures, so you, and your team can focus on the partnership, create stronger relationships, and enjoy the ever lasting experience these trips have to offer.
- Clients of Reel Harbor get to focus all their energy and attention on the essence of the trip and relationships with your team and leave the details of planning and logistics to Reel Harbor.
- Getting out of the office on trips like these helps create even stronger bonds with your team, customer or clients all while creating lifetime memories.
- All of our services are 100% FREE, and you never pay a dime extra for the trip.
- Service is NOT something we talk about, it's something we provide.
- We help customize the itinerary to create a balanced experience for your entire group
- What you can expect on these adventures: team building, employee retention, stronger partnerships, loyalty, growth of company culture, and good lifelong memories!
- We have Hands-on knowledge of the best Lodges for corporate retreats, team building, or exclusive VIP getaways. No matter the need we have you covered!
- What makes us so Great? There's nothing we don't do for you! We take care of everything from booking the trip, the travel, gear that’s needed, travel insurance, special food requirements, etc. And again, we do all of this for FREE!

"The backbone of our business is service and building strong relationships with our clients, outfitters, and employees….Let our team take care of your team”

Target Market(s)

Business's and Corporations

Font styles to use
Serif
Sans Serif

Colors

Designer to choose colors to be used in the design.

Requirements
Must have
• - Excellent Gammer, and a Creative flow.
• - Contact Info and social media links
• Phone: 208-555-0147
• www.reelharbor-example.com
• FB: www.facebook.com/reelharborexpeditions/
• Instagram: @reelharbor
Nice to have
• I would like the brochure to be either a tri-fold or bi-fold. I will leave that up to the designer.
• I am also up for some new design that I may not know about that looks cool and has a good flow.
Should not have
• Small, or hard to read font.

```html
<!DOCTYPE html>
<html lang="en">
<head>
<meta charset="utf-8">
<title>Reel Harbor – Reviews &amp; Why Choose Us</title>
<link href="https://fonts.googleapis.com/css2?family=Yanone+Kaffeesatz:wght@400&family=Tinos:ital@1&family=Open+Sans:wght@400;700&display=swap" rel="stylesheet">
<style>
  :root{
    --ink:#000;
    --steel-dark:#4a5753;
    --steel-mid:#6f7f7a;
    --steel-light:#a4b1ad;
    --bar:#1f2624;
    --tan:#c9b48a;
    --gold:#e0bf84;
    --white:#fff;
    --photo-cool:#8a9ba3;
    --photo-sea:#5f7f92;
  }
  *{margin:0;padding:0;box-sizing:border-box}
  html,body{width:1200px;height:840px;overflow:hidden;background:#fff}
  .brochure{position:relative;width:1200px;height:840px;overflow:hidden;background:#fff}
  .panel{position:absolute;top:0;height:840px;overflow:hidden}
  .panel--reviews{left:0;width:604px;background:linear-gradient(115deg,var(--steel-dark) 0%,var(--steel-light) 40%,var(--steel-mid) 60%,var(--steel-dark) 100%)}
  .panel--why{left:606px;width:594px;background:linear-gradient(120deg,var(--steel-mid) 0%,var(--steel-light) 35%,var(--steel-mid) 65%,var(--steel-dark) 100%)}
  .facets{position:absolute;inset:0}
  .headline{font-family:'Yanone Kaffeesatz',sans-serif;font-weight:400;line-height:1;position:absolute;text-align:center}
  .reviews-title{left:170px;width:374px;top:26px;font-size:70px;color:var(--tan)}
  .reviews-sub{left:170px;width:374px;top:94px;font-size:54px;color:#e4e4e4}
  .why-title{left:0;width:594px;top:30px;font-size:60px;color:var(--white)}
  .why-title .accent{color:var(--tan)}
  .rule{position:absolute;background:var(--bar);height:6px}
  .quote{position:absolute;font-family:'Tinos',serif;font-style:italic;color:#f2f2f2;font-size:23px;line-height:23.5px;white-space:nowrap}
  .author{position:absolute;font-family:'Open Sans',sans-serif;color:var(--gold);font-size:18px;line-height:20px;white-space:nowrap}
  .contact{position:absolute;left:22px;top:764px;width:380px;font-family:'Open Sans',sans-serif;color:#f2f2f2;font-size:14px;line-height:18px;list-style:none}
  .contact b{color:var(--gold);font-weight:700;display:inline-block;width:74px}
  .brand-mark{position:absolute;left:406px;top:640px;width:184px;height:184px;border-radius:50%;background:#3d4a4f;border:4px solid #2a3336;display:flex;align-items:center;justify-content:center;text-align:center}
  .brand-mark span{font-family:'Open Sans',sans-serif;font-weight:700;color:var(--gold);font-size:24px;line-height:1.1}
  .perk{position:absolute;left:44px;font-family:'Open Sans',sans-serif;font-weight:700;color:var(--white);font-size:19.5px;line-height:20.5px;text-shadow:1px 1px 2px rgba(0,0,0,.75);padding-left:22px;white-space:nowrap}
  .perk::before{content:"";position:absolute;left:2px;top:6px;width:9px;height:9px;border-radius:50%;background:var(--white);box-shadow:1px 1px 2px rgba(0,0,0,.6)}
  .photo{position:absolute;border:5px solid var(--ink)}
  .photo--crew{left:380px;top:188px;width:210px;height:218px;background:linear-gradient(180deg,#b9c3c8 0%,var(--photo-cool) 45%,#4b4f52 100%)}
  .photo--floatplane{left:310px;top:650px;width:286px;height:190px;background:linear-gradient(180deg,#7fa6cc 0%,#b8cfe0 40%,var(--photo-sea) 70%,#3e4a4f 100%)}
</style>
</head>
<body>
<main class="brochure">

  <section class="panel panel--reviews">
    <svg class="facets" width="604" height="840" aria-hidden="true">
      <polygon points="120,170 604,170 604,840 60,840" fill="rgba(255,255,255,0.06)"/>
      <polygon points="0,590 604,580 604,840 0,840" fill="rgba(0,0,0,0.12)"/>
      <polygon points="172,6 604,6 604,160 120,160" fill="#000"/>
      <polygon points="0,0 172,0 172,6 120,160 0,540" fill="#000"/>
    </svg>
    <svg class="facets" width="604" height="840" role="img" aria-label="Photo of anglers on a dock with their catch of salmon">
      <defs>
        <linearGradient id="dockTones" x1="0" y1="0" x2="0" y2="1">
          <stop offset="0" stop-color="#8d979b"/>
          <stop offset="0.45" stop-color="#4e5a4a"/>
          <stop offset="1" stop-color="#c3c8cc"/>
        </linearGradient>
      </defs>
      <polygon points="0,0 172,0 118,160 8,540 0,545" fill="url(#dockTones)"/>
    </svg>

    <h2 class="headline reviews-title">Reviews</h2>
    <p class="headline reviews-sub">We’ve Received</p>
    <div class="rule" style="left:120px;top:166px;width:484px;background:#3a4441"></div>

    <p class="quote" style="left:164px;top:193px">“Unbelievable team at reelharbor! Details<br>arethe key when planning a trip of a lifetime<br>and these guys have the details dialed. !”</p>
    <p class="author" style="left:316px;top:283px;width:272px;text-align:center;font-size:17.5px">-- Dennis Holloway - Host of Open<br>Water Journeys TV Show</p>

    <div class="rule" style="left:78px;top:342px;width:512px"></div>

    <p class="quote" style="left:102px;top:381px">“Marcus and Reel Harbor are the real deal. They<br>combine excellent customer service with a true<br>understanding of angling travel issues. I just<br>completed a trip to Russia arranged by Marcus and<br>Reel Harbor &amp; I would highly recommend their<br>services to anyone!”</p>
    <p class="author" style="left:380px;top:538px;width:178px;text-align:right;font-size:19px">-- Dale Stratton</p>

    <div class="rule" style="left:10px;top:580px;width:574px"></div>

    <p class="quote" style="left:54px;top:608px">“Great company with fantastic people and<br>service! Highly recommend! “</p>
    <p class="author" style="left:112px;top:671px;width:270px;text-align:center">-- Anna Fairbank -- Owner of<br>Northwind Travel Boutique</p>

    <div class="rule" style="left:6px;top:750px;width:404px"></div>

    <ul class="contact">
      <li><b>Phone</b>208-555-0147</li>
      <li><b>Web</b>www.reelharbor-example.com</li>
      <li><b>FB</b>facebook.com/reelharborexpeditions/</li>
      <li><b>Instagram</b>@reelharbor</li>
    </ul>

    <div class="brand-mark"><span>Reel<br>Harbor</span></div>
  </section>

  <section class="panel panel--why">
    <svg class="facets" width="594" height="840" aria-hidden="true">
      <polygon points="0,180 260,180 120,840 0,840" fill="rgba(0,0,0,0.08)"/>
      <polygon points="380,180 594,180 594,840 460,840" fill="rgba(255,255,255,0.07)"/>
      <rect x="0" y="8" width="594" height="168" fill="#000"/>
      <rect x="0" y="176" width="594" height="8" fill="#2d3634"/>
    </svg>

    <h2 class="headline why-title">Why <span class="accent">Choose Us</span> For Your<br>Next Fishing Adventure?</h2>

    <p class="perk" style="top:214px">All of our services are 100%<br>FREE &amp; you never pay a<br>dime extra for the trip</p>
    <p class="perk" style="top:288px">Nobody can beat our prices<br>or deals</p>
    <p class="perk" style="top:342px">Nobody cares or has more<br>hands-on knowledge of the<br>best lodges</p>
    <p class="perk" style="top:418px">Huge advantage of working with Reel Harbor is<br>that we have access to the best dates &amp; discounts</p>
    <p class="perk" style="top:474px">Reel Harbor specializes in the most unique and<br>memorable fishing adventures for corporate teams<br>and VIP clients</p>
    <p class="perk" style="top:550px">We can customize each trip to fit your specific<br>needs and requirements</p>
    <p class="perk" style="top:602px">Lodges roll out the red carpet for our clients</p>
    <p class="perk" style="top:640px">We take care of all the<br>little details; Special<br>food requirements,<br>travel, gear, travel<br>insurance, etc.</p>
    <p class="perk" style="top:755px">We plan so you don't<br>have to</p>

    <div class="photo photo--crew" role="img" aria-label="Photo of a fishing group standing on a dock beside a row of halibut"></div>
    <div class="photo photo--floatplane" role="img" aria-label="Photo of anglers walking on a dock away from a floatplane"></div>
  </section>

</main>
</body>
</html>
```